Hush And Look Through Poster for Harbourline Stack Keepers

Task Description
I am the Vice President of Advocacy for the Harbourline Stack Keepers Association. I am looking to have a set of posters made for HALT (Hush And Look Through) in October. HALT is a time when all school children in BC are encouraged to Hush And Look Through for 15-20 minutes at some point in their day.

I would like to get a set of 2 digital posters designed (if possible it would be nice to have the option to print to both 11x17 and 8.5x 11 paper). We need a poster that is high school (Grade 8-12) appropriate and one that is elementary (Grade k-7) appropriate. Both posters need to be replicated in French. All posters need to have the KEU logo on them as well as the Harbourline Stack Keepers Association Logo.

My budget is not huge (whose is?), but we are flexible and open with design. We want posters that appeal to the age groups they are designed for and that promote reading. We would require the digital copy by August 20. Schools will arrange for their own printing as distribution to all the schools in BC is laborious.

Each poster needs to have the following information:

-Hush And Look Through (HALT)
- A Blank Spot that we can add a date to
-the logo for the KEU (attached)
-the logo for the HSKA (attached)- the logos do not have to be large.

Industry/Entity Type

Teacher

Font styles to use
Serif

Requirements
Must have
• -Hush And Look Through (HALT)
• - A Blank Spot that we can add a date to
• -the logo for the KEU (attached)
• -the logo for the HSKA (attached)- the logos do not have to be large.
Nice to have
• Clear Bright Colours
• I have attached last year's posters to give an idea of what we are interested in.

```html
<!DOCTYPE html>
<html lang="en">
<head>
<meta charset="utf-8">
<title>Hush And Look Through – Harbourline Stack Keepers Association</title>
<link rel="stylesheet" href="https://fonts.googleapis.com/css2?family=Archivo+Black&family=Anton&family=Oswald:wght@600;700&family=Open+Sans:wght@400;600&display=swap">
<style>
  :root {
    --green-deep: #2e8a2a;
    --green-mid: #45a83c;
    --green-light: #6cc357;
    --ink: #0b0b0b;
    --paper: #ffffff;
    --footer-green: #45b04a;
  }
  * { margin: 0; padding: 0; box-sizing: border-box; }
  html, body { width: 869px; height: 1200px; overflow: hidden; background: var(--paper); }
  .poster { position: relative; width: 869px; height: 1200px; overflow: hidden; }
  .poster-shapes { position: absolute; inset: 0; width: 869px; height: 1200px; }

  .brand-mark {
    position: absolute; left: 80px; top: 112px;
    display: flex; align-items: center; gap: 14px;
  }
  .brand-square { width: 28px; height: 28px; background: var(--green-mid); }
  .brand-name {
    font-family: "Archivo Black", sans-serif; font-size: 58px; line-height: 1;
    color: var(--ink); letter-spacing: 1px;
  }

  .headline { font-weight: normal; }
  .headline-lead {
    position: absolute; left: 61px; top: 600px;
    font-family: "Archivo Black", sans-serif; font-size: 104px; line-height: 1;
    color: var(--paper); text-shadow: 3px 4px 6px rgba(0,0,0,.45); letter-spacing: 4px;
  }
  .headline-rest {
    position: absolute; left: 61px; top: 728px;
    font-family: "Anton", sans-serif; font-size: 95px; line-height: 1.05;
    color: var(--ink); white-space: nowrap; letter-spacing: 2px;
  }

  .date-bar {
    position: absolute; left: 35px; top: 861px; width: 799px; height: 60px;
    border-radius: 6px;
    background: linear-gradient(#3a3a3a, #111 60%, #000);
    box-shadow: 0 2px 0 #7bd06a, 0 4px 8px rgba(0,0,0,.4);
    display: flex; align-items: center; justify-content: center;
    font-family: "Archivo Black", sans-serif; font-size: 29px; letter-spacing: 1px;
    color: var(--paper); white-space: nowrap;
  }

  .partner-mark {
    position: absolute; left: 60px; top: 996px;
    display: flex; align-items: center; gap: 10px;
  }
  .partner-circle { width: 26px; height: 26px; border-radius: 50%; border: 3px solid var(--ink); }
  .partner-name {
    font-family: "Archivo Black", sans-serif; font-size: 32px; color: var(--ink); line-height: 1;
  }

  .call-label {
    position: absolute; left: 235px; top: 982px;
    font-family: "Oswald", sans-serif; font-weight: 700; font-size: 42px; line-height: 1;
    color: var(--ink); white-space: nowrap;
  }
  .call-number {
    position: absolute; left: 432px; top: 962px;
    font-family: "Oswald", sans-serif; font-weight: 700; font-size: 70px; line-height: 1;
    color: var(--paper); letter-spacing: 1px; white-space: nowrap;
  }

  .footer-contact {
    position: absolute; left: 0; right: 0; top: 1110px;
    text-align: center; padding-left: 130px;
    font-family: "Open Sans", sans-serif;
  }
  .contact-name { font-weight: 600; font-size: 24px; color: var(--footer-green); line-height: 1.2; }
  .contact-address { font-size: 19px; color: var(--paper); line-height: 1.4; word-spacing: 2px; }
</style>
</head>
<body>
<main class="poster">
  <svg class="poster-shapes" viewBox="0 0 852 1091" preserveAspectRatio="none">
    <defs>
      <linearGradient id="paperFade" x1="0" y1="0" x2="0" y2="1">
        <stop offset="0" stop-color="#ffffff"/>
        <stop offset="1" stop-color="#e4e4e4"/>
      </linearGradient>
      <linearGradient id="photoTones" x1="0" y1="0" x2="1" y2="1">
        <stop offset="0" stop-color="#d9c6a8"/>
        <stop offset="0.45" stop-color="#c98456"/>
        <stop offset="0.75" stop-color="#e7d9c8"/>
        <stop offset="1" stop-color="#bd8f5c"/>
      </linearGradient>
      <linearGradient id="shelfTones" x1="0" y1="0" x2="1" y2="0">
        <stop offset="0" stop-color="#eeeeee"/>
        <stop offset="0.6" stop-color="#b9c3d6"/>
        <stop offset="1" stop-color="#c7905c"/>
      </linearGradient>
      <linearGradient id="greenField" x1="0" y1="0" x2="1" y2="1">
        <stop offset="0" stop-color="#2e8a2a"/>
        <stop offset="0.5" stop-color="#4fae40"/>
        <stop offset="1" stop-color="#6cc357"/>
      </linearGradient>
      <linearGradient id="silverBand" x1="0" y1="0" x2="1" y2="0">
        <stop offset="0" stop-color="#8f8f8f"/>
        <stop offset="0.5" stop-color="#f6f6f6"/>
        <stop offset="1" stop-color="#9d9d9d"/>
      </linearGradient>
    </defs>

    <rect class="paper-field" x="0" y="0" width="852" height="1091" fill="url(#paperFade)"/>

    <polygon class="shelf-photo" role="img" aria-label="Photo area: close-up of colourful book spines on a library shelf"
      points="0,250 230,185 328,185 328,420 0,322" fill="url(#shelfTones)" opacity="0.85"/>

    <rect class="hero-photo" role="img" aria-label="Photo area: a mother and young daughter choosing a book from library shelves"
      x="328" y="0" width="524" height="500" fill="url(#photoTones)"/>

    <polygon class="band-silver-top" points="0,318 555,468 852,476 852,490 555,484 0,336" fill="url(#silverBand)"/>
    <polygon class="band-black-top" points="0,336 555,484 852,490 852,508 555,545 0,362" fill="#0b0b0b"/>
    <polygon class="green-field" points="0,362 555,545 852,508 852,1091 0,1091" fill="url(#greenField)"/>

    <polygon class="band-silver-bottom" points="0,998 555,952 852,998 852,1012 555,966 0,1012" fill="url(#silverBand)"/>
    <polygon class="footer-black" points="0,1012 555,966 852,1012 852,1091 0,1091" fill="#0b0b0b"/>
  </svg>

  <div class="brand-mark">
    <span class="brand-square"></span>
    <span class="brand-name">HSKA</span>
  </div>

  <h1 class="headline">
    <span class="headline-lead">HUSH</span>
    <span class="headline-rest">AND LOOK THROUGH</span>
  </h1>

  <div class="date-bar">A BLANK SPOT THAT WE CAN ADD A DATE</div>

  <div class="partner-mark">
    <span class="partner-circle"></span>
    <span class="partner-name">KEU</span>
  </div>

  <div class="call-label">CALL NOW</div>
  <div class="call-number">6045550187</div>

  <footer class="footer-contact">
    <p class="contact-name">Marlene Okafor</p>
    <p class="contact-address">2817-41B Street&nbsp;&nbsp; Tidewater, BC&nbsp; V9R 2K8</p>
  </footer>
</main>
</body>
</html>
```